Brivane - Business Cards for a new venture

create business card for a startup classified business dealing in construction materials, the cards need to have a professional look but modern, more serious than playful, one of the samples must include the official font (attached), please explore using the official colors in the company's logo

Target Market(s)

Energy sector

Contact Information for Business Card

Font styles to use
Other font styles liked:
• suissnord

Requirements
Must have
• corporate colors (in logo attached)
Nice to have
• Official font (in one of the samples) font is : suissnord
Should not have
• Cartoonish look

```html
<!DOCTYPE html>
<html lang="en">
<head>
<meta charset="utf-8">
<title>Brivane – Business Cards</title>
<link rel="stylesheet" href="https://fonts.googleapis.com/css2?family=Michroma&display=swap">
<style>
  :root {
    --bg: #3f5b8c;
    --navy: #13427a;
    --grey: #8e9096;
    --paper: #ffffff;
    --card-w: 960px;
    --card-h: 540px;
  }
  * { box-sizing: border-box; margin: 0; padding: 0; }
  html, body {
    width: 1200px; height: 1200px; overflow: hidden;
    background: var(--bg);
    font-family: "Michroma", sans-serif;
  }
  .sheet {
    width: 1200px; height: 1200px;
    display: flex; flex-direction: column; align-items: center; justify-content: center;
    gap: 40px;
  }
  .card {
    position: relative;
    width: var(--card-w); height: var(--card-h);
    background: var(--paper);
    box-shadow: 0 6px 18px rgba(0,0,0,0.25);
    overflow: hidden;
  }

  /* Back side: framed contact card */
  .card--back .frame {
    position: absolute; inset: 24px;
    border: 5px solid var(--navy);
  }
  .card--back .wordmark-small {
    position: absolute; left: 60px; top: 60px;
    color: var(--grey); font-size: 28px; letter-spacing: 3px;
    text-transform: uppercase;
  }
  .card--back .mobile {
    position: absolute; right: 60px; top: 56px;
    color: var(--navy); font-size: 17px; letter-spacing: 1px;
    text-transform: uppercase;
  }
  .card--back .brand-center {
    position: absolute; left: 0; right: 0; top: 210px;
    display: flex; align-items: center; justify-content: center; gap: 22px;
    color: var(--navy); font-size: 56px; letter-spacing: 6px; text-transform: uppercase;
  }
  .brand-dot {
    width: 26px; height: 26px; border-radius: 50%;
    background: var(--navy);
  }
  .card--back .contact {
    position: absolute; right: 60px; bottom: 60px;
    text-align: left; line-height: 1.45;
  }
  .contact .email { color: var(--navy); font-size: 19px; }
  .contact .address { color: var(--grey); font-size: 18px; }

  /* Front side: banded name card */
  .card--front .band {
    position: absolute; left: 0; right: 0; height: 66px;
    background: var(--navy);
  }
  .card--front .band--top { top: 0; }
  .card--front .band--bottom { bottom: 0; }
  .card--front .brand-corner {
    position: absolute; left: 60px; top: 110px;
    display: flex; align-items: center; gap: 12px;
    color: var(--grey); font-size: 24px; letter-spacing: 3px; text-transform: uppercase;
  }
  .brand-square {
    width: 16px; height: 16px; background: var(--grey);
  }
  .card--front .identity {
    position: absolute; left: 50%; top: 230px;
    transform: translateX(-50%);
    text-align: right;
  }
  .identity .name {
    color: var(--navy); font-size: 44px; letter-spacing: 2px; text-transform: uppercase;
    padding-bottom: 6px;
    border-bottom: 4px solid var(--navy);
    white-space: nowrap;
  }
  .identity .role {
    color: var(--grey); font-size: 26px; letter-spacing: 4px; text-transform: uppercase;
    margin-top: 4px;
  }
</style>
</head>
<body>
<main class="sheet">
  <section class="card card--back" aria-label="Business card, contact side">
    <div class="frame"></div>
    <p class="wordmark-small">Brivane</p>
    <p class="mobile">Mobile: +61000555019</p>
    <div class="brand-center">
      <span class="brand-dot"></span>
      <span>Brivane</span>
    </div>
    <div class="contact">
      <p class="email">Email: user@domain.com</p>
      <p class="address">Office:34, Road#00,</p>
      <p class="address">Area Name</p>
    </div>
  </section>

  <section class="card card--front" aria-label="Business card, name side">
    <div class="band band--top"></div>
    <div class="brand-corner">
      <span class="brand-square"></span>
      <span>Brivane</span>
    </div>
    <div class="identity">
      <p class="name">Daniel Reeve</p>
      <p class="role">Proprietor</p>
    </div>
    <div class="band band--bottom"></div>
  </section>
</main>
</body>
</html>
```